Brave Otter Pet Sitting Postcard

I will be sending these postcards to homes in the neighborhood introducing my pet sitting business.

Include the following on the postcard:
Rosalind Hume
555-318-7294
www.braveotterpetsitting.example
help@braveotterpetsitting.example

```html
<!DOCTYPE html>
<html lang="en">
<head>
<meta charset="utf-8">
<title>Brave Otter Pet Sitting Postcard</title>
<link rel="stylesheet" href="https://fonts.googleapis.com/css2?family=Fredoka:wght@500;600&family=Comfortaa:wght@500;700&family=Bubblegum+Sans&display=swap">
<style>
:root{
  --orange:#f47c12;
  --yellow:#f5c518;
  --slate:#4a6274;
  --white:#ffffff;
  --page:#e9e9ea;
  --ink:#3f5566;
}
*{box-sizing:border-box;margin:0;padding:0}
html,body{width:1200px;height:1177px;overflow:hidden;background:var(--page)}
.canvas{position:relative;width:1200px;height:1177px}
.card{position:absolute;left:232px;width:764px;background:var(--white);overflow:hidden;box-shadow:0 4px 14px rgba(0,0,0,.25)}
.card--front{top:26px;height:548px}
.card--back{top:594px;height:546px}

/* front */
.headline{position:absolute;top:10px;left:0;width:100%;text-align:center;font-family:"Fredoka",sans-serif;font-weight:600;font-size:39px;letter-spacing:1px;color:var(--orange)}
.subhead{position:absolute;top:56px;left:0;width:100%;text-align:center;font-family:"Comfortaa",sans-serif;font-weight:700;font-size:20px;color:var(--ink)}
.front-photo{position:absolute;top:102px;left:0;width:764px;height:300px;background:linear-gradient(100deg,#7e9a6a 0%,#d9d3c4 30%,#efe9dd 50%,#b79a6c 75%,#7d9a5f 100%)}
.pill{position:absolute;top:86px;left:134px;width:508px;height:36px;border-radius:18px;background:var(--orange);border:2px solid var(--white);color:var(--white);font-family:Arial,Helvetica,sans-serif;font-size:25px;line-height:32px;text-align:center}
.front-bands{position:absolute;left:0;top:0}
.brand-seal{position:absolute;left:282px;top:277px;width:204px;height:204px;border-radius:50%;background:var(--white);border:13px solid var(--orange);display:flex;align-items:center;justify-content:center;text-align:center}
.brand-name{font-family:"Comfortaa",sans-serif;font-weight:700;font-size:19px;line-height:1.3;color:var(--ink)}
.services{position:absolute;left:35px;top:362px;color:var(--white);font-family:"Comfortaa",sans-serif}
.services h2{font-family:"Comfortaa",sans-serif;font-weight:700;font-size:21px;letter-spacing:6px;color:var(--yellow);margin-left:42px;margin-bottom:6px}
.services li{list-style:none;font-size:16px;line-height:20px}
.contact{position:absolute;left:520px;top:360px;width:214px;text-align:center}
.contact svg{display:block;margin:0 auto 4px}
.owner{font-family:"Bubblegum Sans",sans-serif;font-size:29px;color:var(--yellow);line-height:1}
.phone{font-family:"Comfortaa",sans-serif;font-weight:500;font-size:36px;color:var(--white);line-height:1.2;white-space:nowrap;margin-left:-20px;margin-right:-20px}
.footer{position:absolute;left:0;bottom:0;width:100%;height:52px;background:var(--white);display:flex;align-items:center;justify-content:space-between;padding:0 16px;font-family:"Comfortaa",sans-serif;font-weight:700;font-size:17px;color:var(--ink)}
.footer span{display:flex;align-items:center;gap:12px}
.icon-dot{width:32px;height:32px;border-radius:50%;background:var(--orange);display:flex;align-items:center;justify-content:center}

/* back */
.back-bands{position:absolute;left:0;top:0}
.tagline{position:absolute;left:22px;top:36px;width:330px;font-family:"Bubblegum Sans",sans-serif;font-size:25px;line-height:28px;letter-spacing:1px;text-transform:uppercase;color:var(--ink)}
.photo-circle{position:absolute;border-radius:50%;border:10px solid var(--slate);box-shadow:0 0 0 4px var(--white)}
.photo-main{left:26px;top:138px;width:252px;height:252px;background:radial-gradient(circle at 45% 55%,#e7d2a4 0%,#c9a86c 40%,#8a9a6a 100%)}
.photo-cat{left:344px;top:164px;width:118px;height:118px;background:radial-gradient(circle at 50% 40%,#e59ac7 0%,#a48a7a 60%,#6f6a60 100%);border-width:8px}
.photo-dog{left:344px;top:296px;width:118px;height:118px;background:radial-gradient(circle at 50% 55%,#f2f2f0 0%,#5a5a5a 45%,#7ea05a 100%);border-width:8px}
.back-brand{position:absolute;left:498px;top:40px;width:130px;text-align:center;font-family:"Comfortaa",sans-serif;font-weight:700;font-size:15px;line-height:1.3;color:var(--ink)}
.stamp{position:absolute;left:641px;top:31px;width:90px;height:104px;border:1.5px solid var(--ink)}
.back-bar{position:absolute;left:0;top:450px;width:100%;height:46px;background:var(--slate);display:flex;align-items:center;justify-content:center;gap:20px}
.back-bar .owner{font-size:36px}
.back-bar .phone{font-size:29px;margin:0}
</style>
</head>
<body>
<div class="canvas">

  <section class="card card--front">
    <h1 class="headline">DO YOU WORRY ABOUT YOUR PETS</h1>
    <p class="subhead">While You are Gone from Home?</p>
    <div class="front-photo" role="img" aria-label="Photo of a ginger cat and a golden retriever sitting at a kitchen table by a window"></div>
    <div class="pill">LET US TAKE THAT WORRY AWAY!</div>
    <svg class="front-bands" width="764" height="548" viewBox="0 0 764 548" aria-hidden="true">
      <path d="M0,336 C130,318 250,322 384,360 C520,326 650,318 764,326 L764,548 L0,548Z" fill="#f5c518"/>
      <path d="M0,350 C130,332 250,336 384,374 C520,340 650,332 764,340 L764,548 L0,548Z" fill="#4a6274"/>
    </svg>
    <div class="brand-seal"><span class="brand-name">Brave Otter<br>Pet Sitting</span></div>
    <div class="services">
      <h2>SERVICES</h2>
      <ul>
        <li>• Pet Sitting • Overnight</li>
        <li>• Pet Taxi • Pooper Scooper</li>
        <li>• Concierge Services</li>
        <li>• Holiday Schedule</li>
      </ul>
    </div>
    <div class="contact">
      <svg width="26" height="26" viewBox="0 0 24 24" aria-hidden="true"><path d="M6.6 10.8a15 15 0 0 0 6.6 6.6l2.2-2.2a1 1 0 0 1 1-.25 11.4 11.4 0 0 0 3.6.57 1 1 0 0 1 1 1V20a1 1 0 0 1-1 1A17 17 0 0 1 3 4a1 1 0 0 1 1-1h3.5a1 1 0 0 1 1 1c0 1.25.2 2.45.57 3.57a1 1 0 0 1-.25 1z" fill="#fff"/></svg>
      <div class="owner">Rosalind Hume</div>
      <div class="phone">555-318-7294</div>
    </div>
    <footer class="footer">
      <span><i class="icon-dot"><svg width="16" height="16" viewBox="0 0 16 16" aria-hidden="true"><circle cx="8" cy="8" r="6.5" fill="none" stroke="#fff" stroke-width="1.5"/><path d="M1.5 8h13M8 1.5c-3 3.5-3 9.5 0 13M8 1.5c3 3.5 3 9.5 0 13" fill="none" stroke="#fff" stroke-width="1.3"/></svg></i>www.braveotterpetsitting.example</span>
      <span>help@braveotterpetsitting.example<i class="icon-dot"><svg width="16" height="12" viewBox="0 0 16 12" aria-hidden="true"><rect x="1" y="1" width="14" height="10" rx="1" fill="none" stroke="#fff" stroke-width="1.5"/><path d="M1 1l7 6 7-6" fill="none" stroke="#fff" stroke-width="1.5"/></svg></i></span>
    </footer>
  </section>

  <section class="card card--back">
    <svg class="back-bands" width="764" height="546" viewBox="0 0 764 546" aria-hidden="true">
      <path d="M0,0 L362,0 C440,120 440,330 362,450 L0,450Z" fill="#4a6274"/>
      <path d="M0,0 L346,0 C424,120 424,330 346,450 L0,450Z" fill="#f5c518"/>
    </svg>
    <p class="tagline">Whatever your pet needs<br>- feeding, dog walking,<br>&nbsp;&nbsp;TLC, playtime, etc.</p>
    <div class="photo-circle photo-main" role="img" aria-label="Photo of a golden puppy resting on a person's shoulder"></div>
    <div class="photo-circle photo-cat" role="img" aria-label="Photo of a tabby cat wearing a pink shower cap"></div>
    <div class="photo-circle photo-dog" role="img" aria-label="Photo of a black and white dog holding a red leash on grass"></div>
    <div class="back-brand">Brave Otter<br>Pet Sitting</div>
    <div class="stamp"></div>
    <div class="back-bar">
      <span class="owner">Rosalind Hume</span>
      <span class="phone">555-318-7294</span>
    </div>
    <footer class="footer">
      <span><i class="icon-dot"><svg width="16" height="16" viewBox="0 0 16 16" aria-hidden="true"><circle cx="8" cy="8" r="6.5" fill="none" stroke="#fff" stroke-width="1.5"/><path d="M1.5 8h13M8 1.5c-3 3.5-3 9.5 0 13M8 1.5c3 3.5 3 9.5 0 13" fill="none" stroke="#fff" stroke-width="1.3"/></svg></i>www.braveotterpetsitting.example</span>
      <span>help@braveotterpetsitting.example<i class="icon-dot"><svg width="16" height="12" viewBox="0 0 16 12" aria-hidden="true"><rect x="1" y="1" width="14" height="10" rx="1" fill="none" stroke="#fff" stroke-width="1.5"/><path d="M1 1l7 6 7-6" fill="none" stroke="#fff" stroke-width="1.5"/></svg></i></span>
    </footer>
  </section>

</div>
</body>
</html>
```